Brimvale Solutions Website Project

We require a design to revamp and existing website for a company that provides online solutions for small the medium sized businesses including web development, online marketing, social media, online business plans, social media and e-commerce. We are looking to use colours that integrate well with the current logo. Our target market are small to medium sized businesses and individuals looking for a trusted adviser to cover all their online services.
Existing website - www.brimvalesolutions.com.au
Updates
Participation payments added.
Storyboard layout mentioned in brief was not attached in error. It will be uploaded shortly.
Storyboard file added.
Target Market(s)
Revamp of existing website - Looking for a professional design in line with the target market of small to medium businesses
Industry/Entity Type
Business
Requirements
Must have
- Refer the attached storyboard layout for the site design and requirements. Basic header, footer and sidebar are to be the same on every page with the content changing to match the requirements on each page. 8 pages in total
Should not have
- No click here text

```html
<!DOCTYPE html>
<html lang="en">
<head>
<meta charset="utf-8">
<title>Brimvale Solutions</title>
<link href="https://fonts.googleapis.com/css2?family=Arimo:wght@400;700&family=Roboto+Condensed:wght@400;700&display=swap" rel="stylesheet">
<style>
:root{
  --green:#5fb62a;
  --green-light:#8ccf3c;
  --green-dark:#3f8e1b;
  --lime:#f2f21c;
  --page:#ececec;
  --card:#fafafa;
  --text:#444;
  --orange:#f39a1e;
  --sky:#8fd3f4;
  --link:#1a9ad6;
  --community:#35589a;
}
*{margin:0;padding:0;box-sizing:border-box}
html,body{width:709px;height:1200px;overflow:hidden}
body{position:relative;background:var(--page);font-family:Arimo,Arial,sans-serif;color:var(--text)}
.abs{position:absolute}
.header{left:0;top:0;width:709px;height:306px;background:linear-gradient(#3a3a3a,#1f1f1f);border-top:2px solid var(--green)}
.brand-mark{left:108px;top:12px;width:44px;height:44px;border-radius:50%;background:#fff}
.brand-name{left:96px;top:62px;width:130px;text-align:center;color:#fff;font-weight:700;font-size:17px;line-height:20px;letter-spacing:.5px}
.account{right:93px;top:6px;font-size:7px;color:#ccc;word-spacing:6px}
.find-us{left:455px;top:61px;font-size:9px;color:#bbb}
.social{width:24px;height:24px;border-radius:50%;background:#2d7fc1;border:2px solid #fff}
.call{right:95px;top:57px;text-align:right;color:#ccc;font-size:7px;line-height:9px}
.call b{display:block;font-weight:400;font-size:9px}
.phone{right:95px;top:78px;color:var(--green-light);font-weight:700;font-size:14px}
.hero{left:83px;top:106px;width:544px;height:159px;border-radius:8px 8px 0 0;background:linear-gradient(#8fcb3a,#5aa924);overflow:hidden}
.hero-photo{left:0;top:0;width:205px;height:159px;background:radial-gradient(circle at 40% 45%,#e9e3d2 0 22%,#b3cf7a 40%,#6aa82c 75%)}
.hero-title{left:200px;top:8px;width:318px;text-align:center;color:#fff;font-weight:700;font-size:29px;line-height:35px}
.hero-title span{color:var(--lime)}
.hero-sub{left:234px;top:86px;width:250px;text-align:center;color:#f3f9e6;font-size:16px;line-height:20.4px}
.nav{left:83px;top:265px;width:544px;height:40px;background:linear-gradient(var(--green-light),var(--green-dark))}
.nav a{position:absolute;top:13px;color:#fff;font-size:9px;text-decoration:none;transform:translateX(-50%)}
.nav .home{left:30px;top:5px;width:35px;height:35px;background:#333;border-radius:3px 3px 0 0;transform:none;text-align:center;padding-top:8px}
.search{left:355px;top:8px;width:183px;height:21px;background:#fff;border-radius:2px}
.search span{position:absolute;left:25px;top:6px;font-size:6.5px;font-style:italic;color:#999}
.go{left:162px;top:0;width:21px;height:21px;background:#333;color:#fff;font-size:7px;font-weight:700;text-align:center;line-height:21px}
.h-cond{font-family:"Roboto Condensed",Arial,sans-serif;font-weight:700;color:#222}
.sub-green{font-family:"Roboto Condensed",Arial,sans-serif;color:var(--green);font-size:10px}
.intro{left:89px;top:366px;width:354px;font-size:6.1px;line-height:9.6px;color:#555}
.intro b{color:#333}
.card{width:171px;height:113px;background:var(--card);border-radius:3px;box-shadow:0 2px 0 #d8d8d8}
.card-art{left:6px;top:18px;width:46px;height:72px;border-radius:6px;background:linear-gradient(#f6c04a,#e2552b)}
.card h3{position:absolute;left:57px;top:10px;font-size:11.5px;color:#333}
.card p{position:absolute;left:58px;top:37px;width:100px;font-size:7.2px;line-height:10px;text-align:justify;color:#555}
.btn{height:20px;border-radius:3px;background:linear-gradient(#7ed33a,#4aa81c);color:#fff;font-family:"Roboto Condensed",Arial,sans-serif;font-size:8.5px;line-height:20px;padding-left:5px}
.btn svg{position:absolute;right:-6px;top:2px}
.card .btn{position:absolute;left:89px;top:84px;width:71px}
.arrow-nav{width:24px;height:24px;border-radius:50%;background:#2a2a2a}
.thumb{top:864px;width:61px;height:61px;border:2px solid #fff;box-shadow:0 0 2px #aaa}
.quote{left:477px;top:318px;width:149px;height:192px;border-radius:4px;background:linear-gradient(var(--green-light),var(--green-dark) 78%,#2e2e2e 78%,#1c1c1c)}
.quote h3{position:absolute;top:7px;width:100%;text-align:center;color:#fff;font-weight:400;font-size:13.5px}
.field{position:absolute;left:12px;width:121px;height:13px;border-radius:2px;background:linear-gradient(#fff,#ddd);font-size:6.5px;color:#555;padding:3px 0 0 6px}
.side-box{left:477px;width:149px;border-radius:3px}
.quick{top:521px;height:126px;background:#e3e3e3}
.quick ul{position:absolute;left:5px;top:24px;width:138px;list-style:none;background:#fafafa}
.quick li{font-size:6.3px;color:#555;height:16.7px;line-height:16px;padding-left:15px;border-bottom:1px dashed #ccc}
.updates{top:663px;height:193px;background:var(--sky)}
.updates .inner{position:absolute;left:5px;top:23px;width:139px;height:150px;background:#fafafa}
.post-item{position:absolute;left:5px;width:128px;font-size:6.2px;line-height:10px;color:#666}
.post-item span{color:var(--link)}
.community{top:874px;height:75px;background:var(--community)}
.community .inner{position:absolute;left:5px;top:22px;width:139px;height:46px;background:#fff}
.footer{left:0;top:982px;width:709px;height:218px;background:linear-gradient(#353535,#262626);border-top:4px solid var(--green)}
.footer h4{position:absolute;top:11px;color:#fff;font-size:10px}
.flist{position:absolute;top:40px;width:108px;list-style:none}
.flist li{font-size:6.5px;color:#ccc;height:16.7px;line-height:14px;padding-left:11px;border-bottom:1px dashed #555;position:relative}
.flist li::before{content:"";position:absolute;left:0;top:4px;border:3px solid transparent;border-left:4px solid var(--orange)}
.post{position:absolute;left:356px;width:110px;font-size:6.3px;line-height:10px;color:#777}
.post b{color:#eee}
.faddr{left:494px;font-size:6.3px;line-height:8px;color:#ccc}
</style>
</head>
<body>

<header class="abs header">
  <div class="abs brand-mark"></div>
  <div class="abs brand-name">BRIMVALE<br>SOLUTIONS</div>
  <div class="abs account">Login | Register</div>
  <div class="abs find-us">Find Us</div>
  <div class="abs social" style="left:436px;top:74px"></div>
  <div class="abs social" style="left:465px;top:74px"></div>
  <div class="abs call">Questions?<b>Call Us Now!</b></div>
  <div class="abs phone">800 - 555 - 0192</div>

  <section class="abs hero">
    <div class="abs hero-photo" role="img" aria-label="Hand holding a compass against a green background"></div>
    <h1 class="abs hero-title">Make <span>navigating</span> your business online easy</h1>
    <p class="abs hero-sub">We provide ongoing service to ensure we are delivering the best solution for your business</p>
  </section>

  <nav class="abs nav">
    <a class="home">Home</a>
    <a style="left:96px">About</a>
    <a style="left:149px">Services</a>
    <a style="left:207px">Portfolio</a>
    <a style="left:264px">Contact</a>
    <div class="abs search">
      <svg class="abs" style="left:6px;top:5px" width="12" height="12" viewBox="0 0 12 12"><circle cx="7" cy="5" r="3.5" fill="none" stroke="#333" stroke-width="1.4"/><path d="M4.5 7.5L1 11" stroke="#333" stroke-width="1.6"/></svg>
      <span>Type search here</span>
      <div class="abs go">GO</div>
    </div>
  </nav>
</header>

<main>
  <h2 class="abs h-cond" style="left:89px;top:325px;font-size:14px">What we CAN?</h2>
  <div class="abs sub-green" style="left:89px;top:343px">Our Services</div>
  <p class="abs intro"><b>Duis autem vel eum iriure dolor in hendrerit in vulputate velit esse molestie consequat, vel illum dolore eu feugiat.</b> nulla facilisis at vero eros et accumsan et iusto odio dignissim qui blandit praesent luptatum zzril delenit augue duis dolore te feugait nulla facilisi. Lorem ipsum dolor sit amet, consectetuer adipiscing elit, sed diam.</p>

  <article class="abs card" style="left:89px;top:417px"><div class="abs card-art" role="img" aria-label="Figure with speech bubbles"></div><h3>Blogs</h3><p>Need a dynamic blog to compliment your business or want a blog for personal expression?</p><div class="btn">Find Out More<svg width="16" height="16" viewBox="0 0 16 16"><circle cx="8" cy="8" r="7" fill="var(--orange)" stroke="#fff" stroke-width="1.5"/><path d="M4 8h6M8 5l3 3-3 3" stroke="#fff" stroke-width="1.6" fill="none"/></svg></div></article>
  <article class="abs card" style="left:271px;top:417px"><div class="abs card-art" role="img" aria-label="Two figures shaking hands"></div><h3>Social Media</h3><p>Fast track business success through the use of social media solutions and strategies.</p><div class="btn">Find Out More<svg width="16" height="16" viewBox="0 0 16 16"><circle cx="8" cy="8" r="7" fill="var(--orange)" stroke="#fff" stroke-width="1.5"/><path d="M4 8h6M8 5l3 3-3 3" stroke="#fff" stroke-width="1.6" fill="none"/></svg></div></article>
  <article class="abs card" style="left:89px;top:545px"><div class="abs card-art" role="img" aria-label="Figure holding tools"></div><h3>Web Development</h3><p style="text-align:left">Website solutions designed and developed to maximise your online footprint.</p><div class="btn">Find Out More<svg width="16" height="16" viewBox="0 0 16 16"><circle cx="8" cy="8" r="7" fill="var(--orange)" stroke="#fff" stroke-width="1.5"/><path d="M4 8h6M8 5l3 3-3 3" stroke="#fff" stroke-width="1.6" fill="none"/></svg></div></article>
  <article class="abs card" style="left:271px;top:545px"><div class="abs card-art" role="img" aria-label="Figure pushing a shopping cart"></div><h3>E-commerce</h3><p>E-commerce solutions tailored to your business goals and objectives to help drive sales.</p><div class="btn">Find Out More<svg width="16" height="16" viewBox="0 0 16 16"><circle cx="8" cy="8" r="7" fill="var(--orange)" stroke="#fff" stroke-width="1.5"/><path d="M4 8h6M8 5l3 3-3 3" stroke="#fff" stroke-width="1.6" fill="none"/></svg></div></article>
  <article class="abs card" style="left:89px;top:674px"><div class="abs card-art" role="img" aria-label="Figure working at a desk"></div><h3>Online Business</h3><p>Online specific business plans designed to help you take your idea to the next level.</p><div class="btn">Find Out More<svg width="16" height="16" viewBox="0 0 16 16"><circle cx="8" cy="8" r="7" fill="var(--orange)" stroke="#fff" stroke-width="1.5"/><path d="M4 8h6M8 5l3 3-3 3" stroke="#fff" stroke-width="1.6" fill="none"/></svg></div></article>
  <article class="abs card" style="left:271px;top:674px"><div class="abs card-art" role="img" aria-label="Figure holding a light bulb"></div><h3>Online Marketing</h3><p>Online marketing solutions developed to enhance your website and grow your business.</p><div class="btn">Find Out More<svg width="16" height="16" viewBox="0 0 16 16"><circle cx="8" cy="8" r="7" fill="var(--orange)" stroke="#fff" stroke-width="1.5"/><path d="M4 8h6M8 5l3 3-3 3" stroke="#fff" stroke-width="1.6" fill="none"/></svg></div></article>

  <h2 class="abs h-cond" style="left:94px;top:827px;font-size:14px">Our Recent Works</h2>
  <div class="abs sub-green" style="left:94px;top:843px">Completed Projects</div>
  <div class="abs arrow-nav" style="left:83px;top:880px"><svg width="24" height="24" viewBox="0 0 24 24"><path d="M14 7l-5 5 5 5" stroke="#fff" stroke-width="1.6" fill="none"/></svg></div>
  <div class="abs thumb" style="left:118px;background:linear-gradient(#e8efe0,#a99056)" role="img" aria-label="Restaurant website project"></div>
  <div class="abs thumb" style="left:192px;background:linear-gradient(#f0e6dc,#fff)" role="img" aria-label="Marketing website project"></div>
  <div class="abs thumb" style="left:266px;background:linear-gradient(#f4f4f4,#dde2e8)" role="img" aria-label="Coming soon page project"></div>
  <div class="abs thumb" style="left:339px;background:linear-gradient(#fff,#c8c8c8)" role="img" aria-label="Business website project"></div>
  <div class="abs arrow-nav" style="left:413px;top:880px"><svg width="24" height="24" viewBox="0 0 24 24"><path d="M10 7l5 5-5 5" stroke="#fff" stroke-width="1.6" fill="none"/></svg></div>
</main>

<aside>
  <form class="abs quote">
    <h3>Request A Quote</h3>
    <div class="field" style="top:28px">First Name</div>
    <div class="field" style="top:48px">Last Name</div>
    <div class="field" style="top:68px">Phone</div>
    <div class="field" style="top:88px">Email</div>
    <div class="field" style="top:106px;height:36px">Message</div>
    <div class="abs btn" style="left:29px;top:157px;width:92px;padding-left:11px">Please Contact Me<svg width="16" height="16" viewBox="0 0 16 16"><circle cx="8" cy="8" r="7" fill="var(--orange)" stroke="#fff" stroke-width="1.5"/><path d="M4 8h6M8 5l3 3-3 3" stroke="#fff" stroke-width="1.6" fill="none"/></svg></div>
  </form>

  <section class="abs side-box quick">
    <h4 class="abs h-cond" style="left:11px;top:8px;font-size:10px">Quick Link</h4>
    <ul><li>Blogs</li><li>Social Media</li><li>Web Development</li><li>E-commerce</li><li>Online Business</li><li>Online Marketing</li></ul>
  </section>

  <section class="abs side-box updates">
    <h4 class="abs h-cond" style="left:11px;top:8px;font-size:10px">Latest Updates</h4>
    <div class="inner">
      <p class="post-item" style="top:7px"><span>@Brimvale</span>: Velit esse molestie consequat, vel illum dolore eu feugiat nulla facilisis. At vero eos et <span>@accusam</span> et justo duo.</p>
      <p class="post-item" style="top:67px;border-top:1px dashed #ccc"><span>@velit_esse</span> molestie consequat, vel illum dolore eu feugiat nulla facilisis. At vero eos et accusam et <span>@justo_duo</span>.</p>
      <p class="post-item" style="top:117px"><span>@molestie</span> consequat, vel illum dolore eu feugiat nulla facilisis. At vero eos et accusam et justo duo.</p>
    </div>
    <div class="abs" style="right:10px;top:177px;font-size:6.3px;color:#1a6fa8">Join conversation</div>
  </section>

  <section class="abs side-box community">
    <h4 class="abs h-cond" style="left:8px;top:6px;font-size:10px;color:#fff">COMMUNITY</h4>
    <div class="inner">
      <div class="abs" style="left:7px;top:6px;width:26px;height:26px;background:linear-gradient(#e4c96a,#5a6b7a)" role="img" aria-label="Profile picture"></div>
      <div class="abs" style="left:40px;top:5px;font-size:6.5px;font-weight:700;color:#3b5998">You</div>
      <div class="abs" style="left:40px;top:24px;width:23px;height:10px;border:1px solid #aab;border-radius:2px;background:#eef;font-size:5.5px;color:#3b5998;text-align:center;line-height:8px">Like</div>
      <div class="abs" style="left:70px;top:26px;font-size:6px;color:#333">86 people like <b>You</b></div>
    </div>
  </section>
</aside>

<footer class="abs footer">
  <h4 style="left:88px">Sitemap</h4>
  <ul class="flist" style="left:90px"><li>Home</li><li>About Us</li><li>Services</li><li>Portfolio</li><li>Contact</li></ul>
  <h4 style="left:222px">Link</h4>
  <ul class="flist" style="left:222px"><li>Terms &amp; Condition</li><li>Privacy Policy</li><li>FAQ</li><li>Help</li><li>Login</li></ul>
  <h4 style="left:354px">Last Blog Post</h4>
  <p class="post" style="top:42px"><b>Duis autem vel eum iriure dolor in hendrerit in vulputate.</b><br>Velit esse molestie consequat, vel illum dolore eu feugiat...</p>
  <p class="post" style="top:92px"><b>Duis autem vel eum iriure dolor in hendrerit in vulputate.</b><br>Velit esse molestie consequat, vel illum doloresis...</p>
  <div class="abs btn" style="left:399px;top:142px;width:58px">More News<svg width="16" height="16" viewBox="0 0 16 16"><circle cx="8" cy="8" r="7" fill="var(--orange)" stroke="#fff" stroke-width="1.5"/><path d="M4 8h6M8 5l3 3-3 3" stroke="#fff" stroke-width="1.6" fill="none"/></svg></div>
  <h4 style="left:493px">Get in touch</h4>
  <div class="abs" style="left:494px;top:39px;width:103px;height:59px;border:2px solid #ddd;background:linear-gradient(135deg,#e9e4d6,#cfd9c4)" role="img" aria-label="Street map of the office location"></div>
  <div class="abs faddr" style="top:114px">14 Harbour Lane, Suite 3<br>Eastbrook City</div>
  <div class="abs faddr" style="top:138px">Website: www.brimvale.com<br>Email: info@brimvale.com<br>Phone: 888 - 555 - 0147</div>
  <div class="abs social" style="left:494px;top:169px"></div>
  <div class="abs social" style="left:522px;top:169px"></div>
  <div class="abs" style="left:86px;top:193px;font-size:6.3px;color:#999">Copyright © 2012 Brimvale.com - All Right Reserved</div>
</footer>

</body>
</html>
```